Steel Company / Iron Railing Business Card Template

We are a custom steel fabrication company located in Harlow Bend, OR. In business since 1979, we recently developed a new logo, and we're looking for a business card design to help display the new logo and our business. The name of the company is Kelbrook Forge Co.. The Office Phone number is (555) 555-0143. We fabricate and install custom "wrought iron" railings on our residential side, we also fabricate and erect structural steel (think cranes and steel beams in buildings) on our commercial side. Looking to get a business card template designed. Something modern, but professional. Clear and easy to read. Front should have all business and employee information including phone number(s), email address, business information, etc. back should spotlight logo.

Industry/Entity Type

Construction / Home Improvement

Contact Information for Business Card

Business information is Kelbrook Forge Co., 48 Dunmore Ave Suite 3305, Harlow Bend, OR 19074. Phone number is (555) 555-0143. Website is www.kelbrookforge.example Business card should be for "Tom Pelling" with the job title "Sales & Estimating" but be editable for other employees. Tom's phone number is (610) 555-0178

Colors

Designer to choose colors to be used in the design.

Requirements
Must have
• Modern Feel, Design should be sized for standard business card sizing 3.5" x 2" (88.9mm x 50.8mm)

```html
<!DOCTYPE html>
<html lang="en">
<head>
<meta charset="utf-8">
<title>Kelbrook Forge Co. — Business Card</title>
<link href="https://fonts.googleapis.com/css2?family=Poppins:wght@400;500;600;700&display=swap" rel="stylesheet">
<style>
  :root {
    --stage: #2b2b2d;
    --card-dark: #0e0e0f;
    --card-light: #ffffff;
    --brand-blue: #22408f;
    --brand-red: #d7242a;
    --text-light: #ffffff;
    --text-soft: #e9ecf5;
  }
  * { box-sizing: border-box; margin: 0; padding: 0; }
  html, body {
    width: 1200px; height: 875px; overflow: hidden;
    background: var(--stage);
    font-family: "Poppins", sans-serif;
  }
  .stage {
    width: 1200px; height: 875px;
    display: flex; align-items: center; justify-content: center; gap: 40px;
  }
  .card {
    width: 520px; height: 297px;
    border-radius: 18px;
    position: relative;
    overflow: hidden;
    box-shadow: 0 18px 40px rgba(0,0,0,.45);
  }

  /* Back card */
  .card--back { background: var(--card-dark); }
  .back__brand {
    position: absolute; top: 62px; left: 0; right: 0;
    display: flex; align-items: center; justify-content: center; gap: 12px;
  }
  .brand-dot {
    width: 16px; height: 16px; border-radius: 50%; background: var(--brand-red); flex: none;
  }
  .brand-name {
    font-weight: 700; font-size: 34px; color: var(--brand-blue); letter-spacing: .5px;
  }
  .services__heading {
    position: absolute; top: 150px; left: 0; right: 0;
    display: flex; align-items: center; justify-content: center; gap: 14px;
    color: var(--brand-blue); font-weight: 700; font-size: 14px; letter-spacing: 1px;
  }
  .services__rule { width: 120px; height: 1px; background: var(--brand-red); }
  .services__list {
    position: absolute; left: 0; right: 0;
    display: flex; justify-content: center; align-items: center; gap: 10px;
    color: var(--text-light); font-size: 12.5px; letter-spacing: .3px;
  }
  .services__list--one { top: 190px; }
  .services__list--two { top: 218px; }
  .bullet { width: 6px; height: 6px; border-radius: 50%; background: var(--brand-red); }

  /* Front card */
  .card--front { background: var(--card-light); }
  .front__brand {
    position: absolute; left: 22px; top: 0; bottom: 0; width: 220px;
    display: flex; align-items: center; justify-content: center; gap: 10px;
  }
  .front__brand .brand-name { font-size: 25px; line-height: 1.15; }
  .contact-panel {
    position: absolute; right: 18px; top: 18px; bottom: 18px; width: 250px;
    background: var(--brand-blue); border-radius: 22px;
    padding: 44px 20px 0 28px; color: var(--text-light);
  }
  .contact__name { font-weight: 600; font-size: 21px; line-height: 1.1; }
  .contact__title { font-size: 12px; color: var(--text-soft); margin-top: 4px; }
  .contact__address { font-size: 11.5px; margin-top: 16px; line-height: 1.45; }
  .contact__list { list-style: none; margin-top: 14px; }
  .contact__item {
    display: flex; align-items: center; gap: 10px;
    font-size: 11.5px; line-height: 1.7; white-space: nowrap;
  }
  .contact__item svg { width: 11px; height: 11px; fill: var(--text-light); flex: none; }
</style>
</head>
<body>
<main class="stage">

  <section class="card card--back" aria-label="Card back">
    <div class="back__brand">
      <span class="brand-dot"></span>
      <span class="brand-name">Kelbrook Forge Co.</span>
    </div>
    <div class="services__heading">
      <span class="services__rule"></span>
      <span>OUR SERVICES</span>
      <span class="services__rule"></span>
    </div>
    <div class="services__list services__list--one">
      <span>Gates</span><span class="bullet"></span>
      <span>Steel Framing</span><span class="bullet"></span>
      <span>Custom Stairways</span><span class="bullet"></span>
      <span>Metal Cutting</span>
    </div>
    <div class="services__list services__list--two">
      <span class="bullet"></span>
      <span>Handrails, Canopies &amp; Balconies</span>
    </div>
  </section>

  <section class="card card--front" aria-label="Card front">
    <div class="front__brand">
      <span class="brand-dot"></span>
      <span class="brand-name">Kelbrook<br>Forge Co.</span>
    </div>
    <div class="contact-panel">
      <h1 class="contact__name">Tom Pelling</h1>
      <p class="contact__title">Sales &amp; Estimating</p>
      <p class="contact__address">48 Dunmore Ave Suite 3305<br>Harlow Bend, OR 19074</p>
      <ul class="contact__list">
        <li class="contact__item">
          <svg viewBox="0 0 24 24" aria-hidden="true"><path d="M6.6 10.8a15.2 15.2 0 0 0 6.6 6.6l2.2-2.2a1 1 0 0 1 1-.25 11.4 11.4 0 0 0 3.6.57 1 1 0 0 1 1 1V20a1 1 0 0 1-1 1A17 17 0 0 1 3 4a1 1 0 0 1 1-1h3.5a1 1 0 0 1 1 1c0 1.25.2 2.45.57 3.57a1 1 0 0 1-.25 1z"/></svg>
          <span>(555) 555-0143</span>
        </li>
        <li class="contact__item">
          <svg viewBox="0 0 24 24" aria-hidden="true"><path d="M2 5h20v14H2zm2 2v.5l8 5 8-5V7l-8 5z"/></svg>
          <span>info@kelbrookforge.example</span>
        </li>
        <li class="contact__item">
          <svg viewBox="0 0 24 24" aria-hidden="true"><path d="M12 2a10 10 0 1 0 0 20 10 10 0 0 0 0-20zm6.9 9h-3a15 15 0 0 0-1.3-5.6A8 8 0 0 1 18.9 11zM12 4c.9 1.2 1.7 3.5 1.9 7h-3.8C10.3 7.5 11.1 5.2 12 4zM9.4 5.4A15 15 0 0 0 8.1 11h-3a8 8 0 0 1 4.3-5.6zM5.1 13h3a15 15 0 0 0 1.3 5.6A8 8 0 0 1 5.1 13zM12 20c-.9-1.2-1.7-3.5-1.900-7h3.8c-.2 3.5-1 5.8-1.9 7zm2.6-1.4a15 15 0 0 0 1.3-5.6h3a8 8 0 0 1-4.3 5.6z"/></svg>
          <span>www.kelbrookforge.example</span>
        </li>
      </ul>
    </div>
  </section>

</main>
</body>
</html>
```